We need a DL size flyer, double sided, for our lawn mowing and gardening business, Kestrel Yards.

We want to run on the front side, the following promotion:
50% off lawn mowing, applies to first lawn mowed on any regular service,
applies to first 100 callers only, so call now!
Professional lawn mowing at an affordable price.

Logo at the bottom left, with Lawn and Garden Maintenance written just below logo.

On bottom Right contact details;
Tom and Gareth
Ph: 0487650912
Email: kestrelyards@mailbox-demo.com
www.kestrelyards-demo.com.au

Front side positioned horizontally, with a bright and colour full design in the background, with the offer of 50% Off lawn mowing in large letters along the top.

On the rear side, also positioned horizontally, a list of our services, stating;

At Kestrel Yards we specialise in the following services;
Lawn mowing
Edging
Blowing
Hedging
Pruning
Tree Loping
Weeding
Poisoning
Mulching
Fertilising
Rubbish removal
Planting
Lawn care and advice
Turf
And any other garden maintenance job,
No job too big or too small.
(No particular order, whatever fits best)
Also include our contact details,
Kestrel Yards
Ph 0487650912
www.kestrelyards-demo.com.au

Target Market(s)

Home owners, aged between 30-50 years old, moderate socio ecenomic status to more afluent areas.

Industry/Entity Type

Business

Requirements
Must have
• DL size, front and back, full colour.
Nice to have
• The writting stating "Kestrel Yards" in our logo is quite bland, if that could also be amended to make it more appealing, but change the writting design only not the actual logo.

```html
<!DOCTYPE html>
<html lang="en">
<head>
<meta charset="utf-8">
<title>Kestrel Yards – DL Flyer</title>
<link href="https://fonts.googleapis.com/css2?family=Lobster&family=Arimo:wght@400;700&display=swap" rel="stylesheet">
<style>
  :root{
    --page:#f3f3f3;
    --leaf:#8ee24a;
    --leaf-dark:#18c22e;
    --leaf-deep:#0f9a1f;
    --sun:#ffd21f;
    --sun-orange:#f7a21f;
    --sky:#52c8f2;
    --white:#ffffff;
    --ink-yellow:#f7e21a;
  }
  *{box-sizing:border-box;margin:0;padding:0}
  html,body{width:1179px;height:1200px;overflow:hidden}
  body{background:var(--page);position:relative;font-family:"Arimo",Arial,sans-serif}

  .flyer{position:absolute;left:116px;width:941px;height:442px;overflow:hidden;
    box-shadow:0 14px 30px rgba(0,0,0,.22)}
  .flyer--front{top:76px}
  .flyer--back{top:664px}

  .backdrop{position:absolute;inset:0}
  .flyer--front .backdrop{
    background:
      radial-gradient(ellipse 55% 45% at 8% 0%, #f08a1c 0%, rgba(240,138,28,0) 70%),
      linear-gradient(180deg,#f5c62a 0%,#e8e04a 20%,#a8d83a 34%,#7cc836 48%,#5fb62a 70%,#6cc52f 100%);
  }
  .flyer--back .backdrop{
    background:
      linear-gradient(180deg,#4cc3ef 0%,#a9e2f7 22%,#e6f6fb 36%,#cfe9ef 40%,#3d8a3a 41%,#2f7b30 47%,#6ccf2d 50%,#59d52a 70%,#4cc524 100%);
  }

  /* signposts */
  .post{position:absolute;background:var(--leaf);bottom:0;box-shadow:2px 0 4px rgba(0,0,0,.12)}
  .sign{position:absolute;display:flex;align-items:center;justify-content:center;text-align:center;
    color:var(--white);box-shadow:0 3px 6px rgba(0,0,0,.15)}
  .sign--left{clip-path:polygon(9% 0,100% 0,100% 100%,9% 100%,0 50%)}
  .sign--right{clip-path:polygon(0 0,91% 0,100% 50%,91% 100%,0 100%)}
  .sign--light{background:var(--leaf)}
  .sign--dark{background:var(--leaf-dark);color:var(--ink-yellow)}

  /* front */
  .offer{position:absolute;font-family:"Lobster",cursive;color:var(--sun);
    text-shadow:0 3px 10px rgba(0,0,0,.25)}
  .offer__amount{left:213px;top:14px;font-size:96px;transform:rotate(-4deg);color:#f8e23a}
  .offer__service{left:200px;top:118px;font-size:66px;transform:rotate(-5deg);color:#c6ef5a;
    -webkit-text-stroke:1.5px var(--white)}

  .promo{font-size:21px;line-height:1.2;padding-left:30px}
  .promo--one{left:588px;top:82px;width:330px;height:88px;transform:rotate(4deg)}
  .promo--two{left:588px;top:184px;width:330px;height:88px;transform:rotate(4deg)}
  .promo--three{left:588px;top:298px;width:330px;height:80px;transform:rotate(-4deg);
    font-family:"Lobster",cursive;font-size:23px}

  .brand{position:absolute;display:flex;align-items:center;gap:10px;font-family:"Lobster",cursive;color:var(--white)}
  .brand__dot{width:22px;height:22px;border-radius:50%;background:var(--sun);flex:none}
  .brand--front{left:40px;top:290px;font-size:34px}
  .brand--back{left:752px;top:52px;font-size:28px}

  .tagline{position:absolute;left:20px;top:398px;width:236px;height:30px;border-radius:6px;
    background:var(--leaf-dark);color:var(--white);font-family:"Lobster",cursive;font-size:16px;
    display:flex;align-items:center;justify-content:center}

  .contact{position:absolute;left:277px;top:334px;color:var(--white);font-size:18px;line-height:22px;
    list-style:none;text-shadow:0 1px 2px rgba(0,0,0,.2)}

  /* back */
  .services-title{position:absolute;left:20px;top:22px;width:440px;text-align:center;
    font-family:"Lobster",cursive;font-size:29px;line-height:1.15;color:var(--leaf-dark);
    -webkit-text-stroke:1px var(--white);paint-order:stroke fill}
  .service{font-size:21px;height:36px}
  .service--small{font-size:16px}

  .closing{position:absolute;font-family:"Lobster",cursive}
  .closing__name{left:498px;top:180px;font-size:62px;transform:rotate(4deg);
    color:#9bf03c;-webkit-text-stroke:1px var(--leaf-deep)}
  .closing__any{left:490px;top:262px;font-size:25px;color:var(--white);transform:rotate(5deg)}
  .closing__size{left:510px;top:306px;font-size:31px;color:var(--white);transform:rotate(5deg)}
  .closing__web{left:490px;top:392px;font-family:"Arimo",Arial,sans-serif;font-weight:700;font-size:25px;
    color:var(--white);letter-spacing:.5px}
</style>
</head>
<body>

<section class="flyer flyer--front" aria-label="Flyer front">
  <div class="backdrop" role="img" aria-label="Sunlit green meadow with wildflowers under an orange sky"></div>

  <h1 class="offer offer__amount">50% off</h1>
  <p class="offer offer__service">lawn mowing</p>

  <div class="post" style="left:758px;top:66px;width:56px"></div>
  <div class="sign sign--left sign--light promo promo--one">applies to first lawn mowed on any regular service</div>
  <div class="sign sign--left sign--dark promo promo--two">applies to first 100 callers only, so call now!</div>
  <div class="sign sign--left sign--light promo promo--three">Professional Lawn Mowing At An Affordable Price</div>

  <div class="brand brand--front"><span class="brand__dot"></span>Kestrel Yards</div>
  <div class="tagline">Lawn and Garden Maintenance</div>

  <ul class="contact">
    <li>Tom and Gareth</li>
    <li>Ph: 0487650912</li>
    <li>Email: kestrelyards@mailbox-demo.com</li>
    <li>www.kestrelyards-demo.com.au</li>
  </ul>
</section>

<section class="flyer flyer--back" aria-label="Flyer back">
  <div class="backdrop" role="img" aria-label="Bright green lawn with a treeline beneath a blue cloudy sky"></div>

  <h2 class="services-title">At Kestrel Yards we specialise in the following services;</h2>

  <div class="post" style="left:113px;top:100px;width:26px"></div>
  <div class="post" style="left:365px;top:100px;width:26px"></div>

  <div class="sign sign--left sign--light service" style="left:12px;top:128px;width:208px">Lawn mowing</div>
  <div class="sign sign--left sign--dark service" style="left:12px;top:170px;width:208px">Edging</div>
  <div class="sign sign--left sign--light service" style="left:12px;top:210px;width:208px">Blowing</div>
  <div class="sign sign--right sign--dark service" style="left:12px;top:252px;width:208px">Hedging</div>
  <div class="sign sign--right sign--light service" style="left:12px;top:292px;width:208px">Pruning</div>
  <div class="sign sign--left sign--light service" style="left:12px;top:332px;width:208px">Tree Loping</div>
  <div class="sign sign--left sign--dark service" style="left:12px;top:374px;width:208px">Weeding</div>

  <div class="sign sign--right sign--dark service" style="left:264px;top:124px;width:208px">Poisoning</div>
  <div class="sign sign--left sign--light service" style="left:264px;top:166px;width:208px">Mulching</div>
  <div class="sign sign--left sign--dark service" style="left:264px;top:208px;width:208px">Fertilising</div>
  <div class="sign sign--light service" style="left:264px;top:250px;width:208px;clip-path:none">Rubbish removal</div>
  <div class="sign sign--right sign--dark service" style="left:264px;top:292px;width:208px">Planting</div>
  <div class="sign sign--right sign--light service service--small" style="left:264px;top:332px;width:208px">Lawn care and advice</div>
  <div class="sign sign--right sign--light service" style="left:264px;top:372px;width:208px">Turf</div>

  <div class="brand brand--back"><span class="brand__dot"></span>Kestrel Yards</div>

  <p class="closing closing__name">Kestrel Yards</p>
  <p class="closing closing__any">And any other garden maintenance job,</p>
  <p class="closing closing__size">No job too big or too small.</p>
  <p class="closing closing__web">www.kestrelyards-demo.com.au</p>
</section>

</body>
</html>
```